Electronic hardware design and manufacturer needing a new business card design.

We need a new business card design consisting of a double sided design adhering to brand and logo guidelines attached. I also want to incorporate something that recognizes our 25th year in business ("EST 2001" or something like that....).

Need extra days to review

Need extra days to review

```html
<!DOCTYPE html>
<html lang="en">
<head>
<meta charset="utf-8">
<title>Vantor Circuits Corp. — Business Card</title>
<link rel="stylesheet" href="https://fonts.googleapis.com/css2?family=Source+Sans+3:wght@400;600;700&display=swap">
<style>
  :root {
    --backdrop: #2b2b2d;
    --card-white: #ffffff;
    --navy: #0f2a3d;
    --navy-deep: #07273b;
    --navy-soft: #0d3550;
    --orange: #f0a21a;
    --rule: #9a9a9a;
    --ink: #1b1b1b;
    --pale-blue: #a9bfd6;
  }
  * { box-sizing: border-box; margin: 0; padding: 0; }
  html, body {
    width: 1200px; height: 1108px; overflow: hidden;
    background: var(--backdrop);
    font-family: "Source Sans 3", sans-serif;
  }
  .sheet {
    position: relative; width: 1200px; height: 1108px;
    display: flex; justify-content: center; align-items: center; gap: 60px;
  }
  .card {
    width: 360px; height: 620px; border-radius: 22px;
    position: relative; overflow: hidden;
  }
  .card--front {
    background: var(--card-white);
    display: flex; flex-direction: column; align-items: center;
    padding: 80px 36px 0;
    text-align: center;
  }
  .brand { display: flex; align-items: center; gap: 12px; }
  .brand__mark {
    width: 22px; height: 22px; border-radius: 50%;
    background: var(--orange);
  }
  .brand__name {
    font-weight: 700; font-size: 72px; line-height: 1;
    color: var(--navy); letter-spacing: 2px;
  }
  .brand__full {
    font-weight: 700; font-size: 15px; letter-spacing: 1.5px;
    color: var(--navy); text-transform: uppercase; margin-top: 10px;
  }
  .person { margin-top: 84px; }
  .person__name {
    font-weight: 700; font-size: 34px; color: var(--navy);
    text-transform: uppercase; line-height: 1;
  }
  .person__role {
    font-weight: 400; font-size: 24px; color: var(--orange);
    text-transform: uppercase; margin-top: 4px; letter-spacing: 0.5px;
  }
  .contact-divider {
    display: flex; align-items: center; gap: 8px;
    width: 100%; margin-top: 26px;
  }
  .contact-divider::before, .contact-divider::after {
    content: ""; flex: 1; height: 1px; background: var(--rule);
  }
  .contact-icon {
    width: 34px; height: 34px; border-radius: 6px;
    background: var(--navy); display: flex; align-items: center; justify-content: center;
  }
  .contact-list {
    list-style: none; margin-top: 12px;
    font-size: 22px; color: var(--ink); line-height: 1.3;
  }
  .rule { width: 100%; height: 1px; background: var(--rule); margin-top: 22px; }
  .address {
    font-style: normal; font-size: 22px; color: var(--ink);
    line-height: 1.3; margin-top: 18px;
  }
  .card--back { background: var(--navy-deep); }
  .back-pattern {
    position: absolute; inset: 0;
    background: radial-gradient(ellipse at 80% 15%, #14537a 0%, var(--navy-soft) 35%, var(--navy-deep) 75%);
  }
  .back-brand {
    position: absolute; left: 0; right: 0; bottom: 90px;
    display: flex; flex-direction: column; align-items: center;
  }
  .back-brand .brand__name { color: var(--pale-blue); font-size: 56px; }
  .back-brand .brand__full { color: var(--pale-blue); font-size: 12px; margin-top: 6px; }
  .established {
    font-weight: 600; font-size: 22px; color: var(--card-white);
    margin-top: 8px; letter-spacing: 0.5px;
  }
</style>
</head>
<body>
  <main class="sheet">
    <section class="card card--front" aria-label="Business card front">
      <div class="brand">
        <span class="brand__name">VCC</span>
        <span class="brand__mark"></span>
      </div>
      <div class="brand__full">Vantor Circuits Corp.</div>

      <div class="person">
        <h1 class="person__name">Marcus Hale</h1>
        <p class="person__role">Managing Director</p>
      </div>

      <div class="contact-divider">
        <span class="contact-icon">
          <svg width="20" height="20" viewBox="0 0 24 24" fill="none" stroke="#fff" stroke-width="2" stroke-linecap="round" stroke-linejoin="round" aria-hidden="true">
            <path d="M22 16.9v3a2 2 0 0 1-2.2 2 19.8 19.8 0 0 1-8.6-3.1 19.5 19.5 0 0 1-6-6A19.8 19.8 0 0 1 2.1 4.2 2 2 0 0 1 4.1 2h3a2 2 0 0 1 2 1.7c.1 1 .4 1.9.7 2.8a2 2 0 0 1-.5 2.1L8 9.9a16 16 0 0 0 6 6l1.3-1.3a2 2 0 0 1 2.1-.4c.9.3 1.8.6 2.8.7a2 2 0 0 1 1.7 2z"/>
          </svg>
        </span>
        <span class="contact-icon">
          <svg width="20" height="20" viewBox="0 0 24 24" fill="none" stroke="#fff" stroke-width="2" stroke-linejoin="round" aria-hidden="true">
            <rect x="3" y="5" width="18" height="14" rx="1"/><path d="M3 6l9 7 9-7"/>
          </svg>
        </span>
        <span class="contact-icon">
          <svg width="20" height="20" viewBox="0 0 24 24" fill="none" stroke="#fff" stroke-width="2" aria-hidden="true">
            <circle cx="12" cy="12" r="9"/><path d="M3 12h18M12 3c3 3 3 15 0 18M12 3c-3 3-3 15 0 18"/>
          </svg>
        </span>
      </div>

      <ul class="contact-list">
        <li>044-987 654 321</li>
        <li>hello@vantorcc.com</li>
        <li>www.vantorcc.com</li>
      </ul>

      <div class="rule"></div>

      <address class="address">
        88, Harbour Road, Unit 4<br>
        20417, Northvale
      </address>
    </section>

    <section class="card card--back" aria-label="Business card back">
      <div class="back-pattern" role="img" aria-label="Repeating tonal brand pattern on deep navy"></div>
      <div class="back-brand">
        <span class="brand__name">VCC</span>
        <span class="brand__full">Vantor Circuits Corp.</span>
        <span class="established">EST 2001</span>
      </div>
    </section>
  </main>
</body>
</html>
```